I need a Label design for my copper 71 kombucha brand that is launching soon

I want a label to go on my copper 71 kombucha bottle.
I have a logo image uploaded in the files but I am open to changes to this logo or even a completely New one if you think you can do better. This logo is based on the idea of an s-shaped naga. I particularly like the nagas from temples in luang prabang.
I also want to include the slogan - dare to be delicious.
The label should be some kind of oval at 80mm high by 70mm wide.
The label will go on a clear glass bottle. The kombucha will be visible and comes in different shades of red,yellow and purple.
The word kombucha should be clearly visible.
i want a very colorful, playful label. I'm very keen to see your ideas and I want something original.
Fermented foods and beverages

```html
<!DOCTYPE html>
<html lang="en">
<head>
<meta charset="utf-8">
<title>copper 71 Kombucha – Bottle Label</title>
<link rel="stylesheet" href="https://fonts.googleapis.com/css2?family=Montserrat:wght@500;800&family=Oswald:wght@700&display=swap">
<style>
  :root {
    --magenta: #c12e7a;
    --magenta-deep: #a8236a;
    --magenta-light: #ef8fbf;
    --white: #ffffff;
    --sun: #f4c325;
    --ink: #222222;
    --leaf: #77a03f;
    --backdrop: #d9d9d9;
  }
  html, body {
    margin: 0;
    padding: 0;
    overflow: hidden;
  }
  body {
    width: 828px;
    height: 1200px;
    background: var(--backdrop);
  }
  .label {
    display: block;
    width: 828px;
    height: 1200px;
  }
  .brand-name {
    font-family: "Montserrat", sans-serif;
    font-weight: 500;
    font-size: 64px;
    fill: var(--magenta);
  }
  .product-name {
    font-family: "Oswald", sans-serif;
    font-weight: 700;
    font-size: 132px;
    fill: var(--white);
  }
  .tagline-lead {
    font-family: "Montserrat", sans-serif;
    font-weight: 800;
    font-size: 32px;
    fill: var(--ink);
  }
  .tagline-main {
    font-family: "Montserrat", sans-serif;
    font-weight: 800;
    font-size: 48px;
    fill: var(--leaf);
  }
</style>
</head>
<body>
<svg class="label" viewBox="0 0 828 1200" xmlns="http://www.w3.org/2000/svg" role="img" aria-label="copper 71 kombucha oval label, Dare to be delicious">
  <defs>
    <linearGradient id="rim-sheen" x1="0" y1="0" x2="1" y2="1">
      <stop offset="0" stop-color="var(--magenta)"/>
      <stop offset="0.45" stop-color="var(--magenta)"/>
      <stop offset="0.6" stop-color="var(--magenta-light)"/>
      <stop offset="0.75" stop-color="var(--magenta)"/>
      <stop offset="1" stop-color="var(--magenta-deep)"/>
    </linearGradient>
    <clipPath id="label-face">
      <ellipse cx="414" cy="600" rx="348" ry="408"/>
    </clipPath>
    <path id="tagline-arc" d="M 214 884 Q 414 858 614 884"/>
  </defs>

  <!-- Outer rim and face -->
  <ellipse class="label-rim" cx="414" cy="600" rx="372" ry="432" fill="url(#rim-sheen)"/>
  <ellipse class="label-face" cx="414" cy="600" rx="348" ry="408" fill="var(--white)"/>
  <ellipse class="label-inner-line" cx="414" cy="600" rx="334" ry="394" fill="none" stroke="var(--magenta)" stroke-width="2"/>

  <!-- Central band -->
  <g class="product-band" clip-path="url(#label-face)">
    <path d="M 40 510 Q 414 610 788 510 L 788 790 Q 414 720 40 790 Z" fill="var(--magenta)"/>
    <!-- Light strokes under the band -->
    <path d="M 152 812 Q 200 776 268 756 Q 210 786 152 812 Z" fill="var(--white)"/>
    <path d="M 676 812 Q 628 776 560 756 Q 618 786 676 812 Z" fill="var(--white)"/>
  </g>

  <!-- Yellow accents above the band -->
  <path class="accent-left" d="M 112 470 Q 100 488 122 498 Q 180 530 242 557 Q 170 500 138 476 Q 124 464 112 470 Z" fill="var(--sun)"/>
  <path class="accent-right" d="M 716 470 Q 728 488 706 498 Q 648 530 586 557 Q 658 500 690 476 Q 704 464 716 470 Z" fill="var(--sun)"/>

  <!-- Brand mark -->
  <circle class="brand-dot" cx="414" cy="352" r="50" fill="none" stroke="var(--magenta)" stroke-width="10"/>
  <text class="brand-name" x="414" y="482" text-anchor="middle">copper 71</text>
  <line x1="268" y1="520" x2="350" y2="520" stroke="#555555" stroke-width="2"/>
  <line x1="478" y1="520" x2="560" y2="520" stroke="#555555" stroke-width="2"/>

  <!-- Product name -->
  <text class="product-name" x="414" y="712" text-anchor="middle" textLength="600" lengthAdjust="spacingAndGlyphs">KOMBUCHA</text>

  <!-- Tagline -->
  <text class="tagline-lead" x="414" y="832" text-anchor="middle">DARE TO BE</text>
  <text class="tagline-main"><textPath href="#tagline-arc" startOffset="50%" text-anchor="middle">DELICIOUS</textPath></text>
</svg>
</body>
</html>
```